Larkfield Electrical Solar Energy Marketing Flyer

Seeking a flyer to market our electrical business - promoting solar energy systems. Will be used as print marketing.

Attached are similar examples in the industry, as well as current Larkfield Electrical ads and our new "Larkfield Electrical, Air & Solar" logo.

We would like the reverse side to have information relating to solar for business.

This flyer is to promote the solar arm of our business, however we also deliver electrical and air-conditioning services. If possible it would be great to have a small reference to our air-conditioning service on the front page.We also need to reference the we have finance available.
Updates

Project Deadline Extended Reason: Apologies - due to illness I had been unable to complete the required text copy for flyer. Please note any slight changes to brief and copy will be updated urgently today while I am back in the office. There are some great flyers catching our eye. Added Monday, July 18, 2016

Target Market(s)

Home and Business Owners

Industry/Entity Type

Solar Energy

Logo Text

Larkfield Electrical, Air & Solar

Requirements
Must have
• Company logo, NPA installer logo, Finvora Logo, phone number and all licences stated on the attached Larkfield Electrical ad. Catchy, uncomplicated appearance. Colours and pics to compliment logo. Disclaimer
Nice to have
• Testimonial

```html
<!DOCTYPE html>
<html lang="en">
<head>
<meta charset="utf-8">
<title>Larkfield Electrical – Solar for Business</title>
<link rel="stylesheet" href="https://fonts.googleapis.com/css2?family=Russo+One&family=Saira+Semi+Condensed:ital,wght@0,400;0,500;1,400;1,500&family=Exo+2:ital,wght@0,700;1,500&display=swap">
<style>
  :root{
    --maroon:#8a1a1b;
    --red:#d0282e;
    --coral:#db5f63;
    --blush:#f2c5c6;
    --paper:#fbf0ef;
    --orange:#c9502e;
    --footnote:#e07a6a;
    --white:#ffffff;
  }
  html,body{margin:0;padding:0;overflow:hidden;background:var(--white);}
  .flyer{position:relative;width:849px;height:1200px;overflow:hidden;background:var(--white);
    font-family:"Saira Semi Condensed",sans-serif;color:var(--maroon);}
  .flyer-shapes{position:absolute;inset:0;}
  .brand{position:absolute;left:46px;top:40px;display:flex;align-items:center;gap:10px;}
  .brand-dot{width:40px;height:40px;border-radius:50%;background:var(--red);}
  .brand-name{font-family:"Russo One",sans-serif;font-size:23px;color:var(--maroon);}
  .segment{position:absolute;right:31px;top:50px;font-style:italic;font-size:18px;color:var(--orange);}
  .headline{position:absolute;right:31px;top:88px;margin:0;font-family:"Russo One",sans-serif;
    font-weight:400;font-size:31px;color:var(--maroon);letter-spacing:.3px;}
  .tagline{position:absolute;right:31px;top:142px;margin:0;font-family:"Exo 2",sans-serif;
    font-style:italic;font-weight:500;font-size:17px;letter-spacing:2.4px;color:var(--maroon);}
  .contact{position:absolute;right:31px;top:196px;margin:0;text-align:right;font-family:"Exo 2",sans-serif;
    font-style:italic;font-weight:500;font-size:14.5px;line-height:20.4px;color:var(--red);}
  .badge{position:absolute;left:36px;top:437px;width:56px;height:56px;border-radius:50%;
    background:radial-gradient(circle,var(--white) 30%,#f08a3a 32%,#f4a05a 100%);}
  .intro{position:absolute;left:34px;margin:0;font-size:13.6px;line-height:22.9px;
    text-transform:uppercase;letter-spacing:.3px;color:var(--maroon);}
  .intro-company{top:508px;}
  .intro-team{top:645px;}
  .cross-sell{position:absolute;left:33px;top:811px;margin:0;font-style:italic;font-size:13px;
    line-height:19px;text-transform:uppercase;color:var(--red);}
  .finance-title{position:absolute;left:49px;top:920px;margin:0;font-family:"Exo 2",sans-serif;
    font-weight:700;font-size:30px;letter-spacing:3.2px;color:var(--maroon);}
  .finance-title sup{font-size:18px;letter-spacing:2px;}
  .quote-call{position:absolute;left:0;top:1009px;width:448px;height:67px;background:var(--coral);}
  .quote-call-title{position:absolute;left:32px;top:6px;margin:0;font-size:23px;font-weight:500;color:var(--white);}
  .quote-call-phone{position:absolute;left:33px;top:38px;margin:0;font-family:"Exo 2",sans-serif;
    font-style:italic;font-weight:500;font-size:17px;color:var(--maroon);}
  .disclaimer{position:absolute;left:33px;top:1153px;margin:0;font-size:12.7px;color:var(--footnote);}
</style>
</head>
<body>
<div class="flyer">
  <svg class="flyer-shapes" width="849" height="1200" viewBox="0 0 849 1200" aria-hidden="false">
    <defs>
      <linearGradient id="photoTone" x1="0" y1="0" x2="1" y2="1">
        <stop offset="0" stop-color="#d9bfc0"/>
        <stop offset="0.55" stop-color="#b18689"/>
        <stop offset="1" stop-color="#7a4f52"/>
      </linearGradient>
    </defs>
    <polygon class="paper-field" points="0,340 849,540 849,1200 0,1200" fill="var(--paper)"/>
    <rect class="finance-band" x="0" y="870" width="849" height="139" fill="var(--blush)"/>
    <polygon class="hero-band" points="0,155 628,327 728,512 0,340" fill="var(--maroon)"/>
    <polyline class="dotted-rule" points="0,126 645,307 764,520" fill="none" stroke="var(--maroon)"
      stroke-width="3" stroke-linecap="round" stroke-dasharray="0 7"/>
    <polygon class="installer-photo" role="img" aria-label="Photo of a smiling electrician in a hard hat beside rooftop solar panels"
      points="335,429 849,543 849,1121" fill="url(#photoTone)" stroke="var(--white)" stroke-width="6" stroke-linejoin="miter"/>
  </svg>

  <div class="brand"><span class="brand-dot"></span><span class="brand-name">Larkfield Electrical</span></div>
  <p class="segment">business</p>
  <h1 class="headline">DO YOU WANT TO START SAVING?</h1>
  <p class="tagline">INSTALL SOLAR TODAY.</p>
  <p class="contact">tom@larkfieldelectrical.com.au<br>MARLOW CREEK QLD 4580<br>Licence: 58231<br>NPA Accreditation:<br>A0917452</p>

  <div class="badge" role="img" aria-label="NPA accredited installer badge"></div>

  <p class="intro intro-company">We are a family owned business<br>providing solar energy installations<br>as well as air-conditioning and general<br>electrical services throughout<br>South East Queensland.</p>
  <p class="intro intro-team">Tom is our licenced electrician and solar<br>energy designer &amp; installer with a depth of<br>knowledge to better assist our customers. We<br>pride ourselves on providing outstanding customer<br>service, listening to customer needs<br>&nbsp;and assisting in providing the most efficient<br>solutions</p>
  <p class="cross-sell">Why not combine your solar installation with new air-conditioning or<br>electrical improvements - finance available.</p>

  <h2 class="finance-title">FINANCE AVAILABLE<sup>**</sup></h2>

  <div class="quote-call">
    <p class="quote-call-title">CALL US FOR A FREE QUOTE!</p>
    <p class="quote-call-phone">1300 482 907</p>
  </div>

  <p class="disclaimer">**Finance Available to approved applicants. All information correct at time of print. Subject to changes.</p>
</div>
</body>
</html>
```